Crestline Lending Group Business Cards

We are looking to revamp the current business cards each of our locations uses. We are a lending company that specializes in personal loans, title loans, and tax services. We have locations in New Mexico, Texas, and Oklahoma.

We would like a cleaner, sleeker look while still highlighting what we offer. Title Loans, Personal Loans & Tax Services. We also want to include our referral fee somewhere on the card. We would like to see an English option as well as a Spanish option for the cards.

PLEASE NOTE: Some business cards do not include the employee's name but just the store's location, while others will include both.

These are double-sided business cards, and we would like to see proof if possible. I have included proofs of our current business cards for you to review below, as well as our company logo. Feel free to get creative with the logo, etc! Colors should match the logo; however, you do not need to use all of our logo colors if you don't want to.

```html
<!DOCTYPE html>
<html lang="en">
<head>
<meta charset="utf-8">
<title>Crestline Lending Group Business Cards</title>
<link href="https://fonts.googleapis.com/css2?family=Montserrat:wght@300;400;600;700;800&family=Roboto:wght@400&family=Open+Sans:wght@400&display=swap" rel="stylesheet">
<style>
  :root {
    --backdrop: #333333;
    --white: #ffffff;
    --forest: #0f4a2a;
    --forest-dark: #1b2b1a;
    --orange: #f58a20;
    --orange-fold: #e8561c;
    --yellow: #fdd00a;
    --lime: #7ac142;
    --red: #c0202a;
    --ink: #2a2a2a;
  }
  * { margin: 0; padding: 0; box-sizing: border-box; }
  html, body { width: 1200px; height: 1200px; overflow: hidden; background: var(--backdrop); }
  .stage { position: relative; width: 1200px; height: 1200px; }

  .card { position: absolute; width: 679px; height: 407px; border-radius: 3px; box-shadow: 4px 5px 8px rgba(0,0,0,.45); }

  /* Front card */
  .card-front { left: 116px; top: 273px; background: var(--white); z-index: 2; }
  .front-brand { position: absolute; left: 0; top: 0; width: 361px; height: 407px; }
  .brand-name { position: absolute; left: 0; width: 361px; top: 143px; text-align: center;
    font-family: 'Montserrat', sans-serif; font-weight: 700; font-size: 21px; color: var(--forest); }
  .referral { position: absolute; left: 0; width: 361px; top: 236px; text-align: center;
    font-family: 'Montserrat', sans-serif; font-weight: 300; font-size: 16px; line-height: 19px; color: var(--ink); }
  .referral-amount { display: block; margin-top: 2px; font-weight: 800; font-size: 46px; line-height: 52px; color: var(--red); }

  .front-contact { position: absolute; left: 361px; top: 0; width: 318px; height: 407px;
    background: linear-gradient(to right, var(--forest-dark) 0 24px, var(--forest) 24px); border-radius: 0 3px 3px 0; }
  .person { position: absolute; right: 100px; top: 61px; text-align: right; color: var(--white); font-family: 'Montserrat', sans-serif; }
  .person-name { font-weight: 700; font-size: 22px; line-height: 24px; }
  .person-title { font-weight: 300; font-size: 15px; line-height: 18px; }

  .icon-tile { position: absolute; width: 33px; height: 33px; border-radius: 3px; display: flex; align-items: center; justify-content: center; }
  .icon-tile.orange { background: var(--orange); }
  .icon-tile.white { background: var(--white); }

  .contact-band { position: absolute; left: -23px; top: 134px; width: 341px; height: 139px; background: var(--orange); }
  .fold { position: absolute; left: -23px; width: 23px; height: 17px; }
  .fold-top { top: 117px; }
  .fold-bottom { top: 273px; }

  .band-text { position: absolute; color: var(--white); font-family: 'Roboto', sans-serif; }
  .phones { left: 83px; top: 17px; font-size: 16px; line-height: 21px; }
  .web { left: 76px; top: 79px; font-size: 17.5px; line-height: 21px; }

  .address { position: absolute; right: 100px; top: 305px; text-align: right; color: var(--white);
    font-family: 'Roboto', sans-serif; font-size: 17px; line-height: 21px; }

  /* Back card */
  .card-back { left: 441px; top: 604px; background: var(--yellow); z-index: 1; overflow: hidden; }
  .back-name { position: absolute; left: 0; width: 679px; top: 184px; text-align: center;
    font-family: 'Montserrat', sans-serif; font-weight: 700; font-size: 30px; color: var(--forest); }
  .lime-stripe { position: absolute; left: 0; top: 304px; width: 100%; height: 8px; background: var(--lime); }
  .back-footer { position: absolute; left: 0; top: 318px; width: 100%; height: 89px; background: var(--forest); }
  .back-web { position: absolute; left: 0; width: 100%; top: 12px; display: flex; justify-content: center; align-items: center; gap: 14px;
    color: var(--white); font-family: 'Open Sans', sans-serif; font-size: 15px; }
</style>
</head>
<body>
<div class="stage">

  <section class="card card-back">
    <div class="back-name">Crestline Lending Group</div>
    <div class="lime-stripe"></div>
    <div class="back-footer">
      <div class="back-web">
        <svg width="15" height="15" viewBox="0 0 16 16" aria-hidden="true">
          <circle cx="8" cy="8" r="7" fill="none" stroke="#fff" stroke-width="1.3"/>
          <path d="M2 5 Q8 7 14 5 M2 11 Q8 9 14 11 M6 1.5 Q10 8 6 14.5" fill="none" stroke="#fff" stroke-width="1.1"/>
        </svg>
        <span>www.crestlinelend.com</span>
      </div>
    </div>
  </section>

  <section class="card card-front">
    <div class="front-brand">
      <div class="brand-name">Crestline Lending Group</div>
      <p class="referral">REFER A FRIEND<br>GET UP TO<span class="referral-amount">$100</span></p>
    </div>

    <div class="front-contact">
      <div class="person">
        <div class="person-name">DANIEL REYES</div>
        <div class="person-title">CEO MARKETING</div>
      </div>
      <div class="icon-tile orange" style="left:236px; top:64px;">
        <svg width="20" height="22" viewBox="0 0 20 22" aria-hidden="true">
          <circle cx="10" cy="6" r="5" fill="#fff"/>
          <path d="M1 21 Q1 12 10 12 Q19 12 19 21 Z" fill="#fff"/>
        </svg>
      </div>

      <svg class="fold fold-top" viewBox="0 0 23 17" aria-hidden="true"><polygon points="0,17 23,0 23,17" fill="var(--orange-fold)"/></svg>
      <svg class="fold fold-bottom" viewBox="0 0 23 17" aria-hidden="true"><polygon points="0,0 23,0 23,17" fill="var(--orange-fold)"/></svg>

      <div class="contact-band">
        <div class="icon-tile white" style="left:23px; top:22px;">
          <svg width="20" height="20" viewBox="0 0 24 24" aria-hidden="true">
            <path d="M6.6 2.5 L9.5 7 L7.6 9 Q9.5 13.5 14.5 16.5 L16.5 14.5 L21 17.5 L19 21.5 Q12 22 6.5 15 Q2 9 3.5 4 Z" fill="var(--orange)"/>
          </svg>
        </div>
        <p class="band-text phones">+0015 - 2468 - 13579<br>+0015 - 2468 - 13579</p>

        <div class="icon-tile white" style="left:23px; top:82px;">
          <svg width="20" height="18" viewBox="0 0 20 18" aria-hidden="true">
            <rect x="1" y="1" width="18" height="12" rx="1" fill="var(--orange)"/>
            <rect x="3" y="3" width="14" height="7" fill="#fff"/>
            <rect x="8" y="13" width="4" height="3" fill="var(--orange)"/>
            <rect x="5" y="16" width="10" height="2" fill="var(--orange)"/>
          </svg>
        </div>
        <p class="band-text web">hello@crestlinelend.com<br>www.crestlinelend.com</p>
      </div>

      <p class="address">Main Street office,<br>North Avenue 456</p>
      <div class="icon-tile orange" style="left:236px; top:310px;">
        <svg width="22" height="20" viewBox="0 0 22 20" aria-hidden="true">
          <path d="M1 10 L11 1 L21 10" fill="none" stroke="#fff" stroke-width="2.4" stroke-linejoin="round"/>
          <path d="M4 9 L11 3 L18 9 V19 H13 V13 H9 V19 H4 Z" fill="#fff"/>
        </svg>
      </div>
    </div>
  </section>

</div>
</body>
</html>
```